Dental Business Card

I need Dental oriented business cards.
On the front side -
- on the first line, my name:
Dr Marlo Vintner
- on the second line (just underneath):
Doctor of Dental Medicine
- on the third line, or underneath that or in a corner, I would like the address and phone number:
5182 Ch. Birchfield
Montreal QC H2T 4B9
514-629-5074
- other than that i would maybe like a logo of a tooth, but i want it to be subtle and very basic!
- I would like the card to be preferably black or dark grey-ish with the writing in white
On the other side -
- 2-3 lines with the possibility to write the next appointment the box with the lines should be white, with the rest of the card being black

```html
<!DOCTYPE html>
<html lang="en">
<head>
<meta charset="utf-8">
<title>Dr Marlo Vintner – Business Card</title>
<link href="https://fonts.googleapis.com/css2?family=Montserrat:wght@400;500;600&display=swap" rel="stylesheet">
<style>
  :root {
    --page-bg: #e6e7ea;
    --card-dark: #2c2c2c;
    --card-black: #232323;
    --teal: #1fa9b2;
    --white: #ffffff;
    --ink: #3a3a3a;
    --rule: #555555;
  }
  * { box-sizing: border-box; margin: 0; padding: 0; }
  html, body { width: 1200px; height: 800px; overflow: hidden; }
  body {
    background: var(--page-bg);
    font-family: "Montserrat", Arial, sans-serif;
    display: flex;
    align-items: center;
    justify-content: center;
    gap: 40px;
  }
  .card {
    width: 540px;
    height: 310px;
    position: relative;
    color: var(--white);
  }
  .card--front { background: var(--card-dark); }
  .card--back { background: var(--card-black); }

  /* Front */
  .brand {
    position: absolute;
    top: 62px;
    left: 0; right: 0;
    display: flex;
    flex-direction: column;
    align-items: center;
  }
  .brand__row { display: flex; align-items: center; gap: 14px; }
  .brand__dot {
    width: 34px; height: 34px;
    border: 3px solid var(--teal);
    border-radius: 50%;
  }
  .brand__name {
    color: var(--teal);
    font-weight: 500;
    font-size: 30px;
    letter-spacing: 0.04em;
  }
  .brand__tagline {
    margin-top: 8px;
    display: flex; align-items: center; gap: 10px;
    font-size: 16px;
    margin-left: 48px;
  }
  .brand__tagline::before, .brand__tagline::after {
    content: ""; width: 34px; height: 1px; background: var(--white);
  }
  .details {
    position: absolute;
    left: 56px; right: 40px; bottom: 46px;
    display: flex;
    align-items: center;
  }
  .person { text-align: right; padding-right: 22px; width: 220px; }
  .person__name { color: var(--teal); font-weight: 600; font-size: 17px; }
  .person__title { font-size: 13px; margin-top: 3px; }
  .divider { width: 1px; height: 70px; background: var(--white); }
  .contact { padding-left: 22px; font-size: 13px; line-height: 1.5; }
  .contact__phone { display: flex; align-items: center; gap: 6px; }
  .contact__phone svg { width: 12px; height: 12px; fill: var(--teal); }

  /* Back */
  .appointment {
    position: absolute;
    top: 28px; left: 30px; right: 30px;
    height: 210px;
    background: var(--white);
    color: var(--ink);
    padding: 14px 20px;
  }
  .appointment__title {
    text-align: center;
    color: var(--teal);
    font-weight: 600;
    font-size: 18px;
    letter-spacing: 0.03em;
  }
  .weekdays {
    display: flex; justify-content: space-between;
    margin-top: 12px; font-size: 12px;
  }
  .weekday { display: flex; align-items: center; gap: 5px; }
  .weekday__box { width: 14px; height: 14px; border: 1.5px solid var(--teal); }
  .slot {
    display: flex; align-items: flex-end; gap: 6px;
    font-size: 12px; margin-top: 16px;
  }
  .slot__line { border-bottom: 1px solid var(--rule); height: 14px; }
  .slot__line--date { flex: 1; }
  .slot__line--time { width: 90px; }
  .slot__ampm { font-size: 11px; line-height: 1.05; text-align: center; }
  .notice {
    position: absolute;
    bottom: 28px; left: 0; right: 0;
    text-align: center;
    font-size: 13px;
  }
</style>
</head>
<body>
  <section class="card card--front">
    <div class="brand">
      <div class="brand__row">
        <span class="brand__dot"></span>
        <span class="brand__name">Dr Marlo Vintner</span>
      </div>
      <div class="brand__tagline">Dental Medicine</div>
    </div>
    <div class="details">
      <div class="person">
        <p class="person__name">Dr Marlo Vintner</p>
        <p class="person__title">Doctor of Dental Medicine</p>
      </div>
      <div class="divider"></div>
      <div class="contact">
        <p>5182 Ch. Birchfield</p>
        <p>Montreal QC H2T 4B9</p>
        <p class="contact__phone">
          <svg viewBox="0 0 24 24" aria-hidden="true"><path d="M6.6 10.8a15.1 15.1 0 0 0 6.6 6.6l2.2-2.2a1 1 0 0 1 1-.25 11.4 11.4 0 0 0 3.6.57 1 1 0 0 1 1 1V20a1 1 0 0 1-1 1A17 17 0 0 1 3 4a1 1 0 0 1 1-1h3.5a1 1 0 0 1 1 1c0 1.25.2 2.45.57 3.57a1 1 0 0 1-.25 1z"/></svg>
          514-629-5074
        </p>
      </div>
    </div>
  </section>

  <section class="card card--back">
    <div class="appointment">
      <h2 class="appointment__title">NEXT APPOINTMENT</h2>
      <div class="weekdays">
        <span class="weekday"><span class="weekday__box"></span>Mon</span>
        <span class="weekday"><span class="weekday__box"></span>Tue</span>
        <span class="weekday"><span class="weekday__box"></span>Wed</span>
        <span class="weekday"><span class="weekday__box"></span>Thu</span>
        <span class="weekday"><span class="weekday__box"></span>Fri</span>
        <span class="weekday"><span class="weekday__box"></span>Sat</span>
      </div>
      <div class="slot"><span>Date:</span><span class="slot__line slot__line--date"></span><span>Time:</span><span class="slot__line slot__line--time"></span><span class="slot__ampm">am<br>pm</span></div>
      <div class="slot"><span>Date:</span><span class="slot__line slot__line--date"></span><span>Time:</span><span class="slot__line slot__line--time"></span><span class="slot__ampm">am<br>pm</span></div>
      <div class="slot"><span>Date:</span><span class="slot__line slot__line--date"></span><span>Time:</span><span class="slot__line slot__line--time"></span><span class="slot__ampm">am<br>pm</span></div>
    </div>
    <p class="notice">If unable to keep an appointment, kindly give 24 hrs. notice.</p>
  </section>
</body>
</html>
```